Q-Rolls Business Card

We are a modern retail clothing store. Established in 1994. I need a presentable card that will amaze vendors when given to them.

Front: Logo in middle
Info Side:

Name: Tomas Velder
Cell: 630-812-4463
Work: 630-917-3384 EXT. 417
Email: Tomas@q-rolls-example.com
Website: www.Q-rolls-example.com

Industry/Entity Type

Business

```html
<!DOCTYPE html>
<html lang="en">
<head>
<meta charset="utf-8">
<title>Q-Rolls Business Card</title>
<link href="https://fonts.googleapis.com/css2?family=Arimo:wght@400;700&family=Tinos:wght@700&display=swap" rel="stylesheet">
<style>
  :root {
    --ink: #0b0b0b;
    --paper: #ffffff;
    --paper-shade: #e9e9e9;
    --rule: #8a8a8a;
    --backdrop: #d9d4cc;
  }
  * { margin: 0; padding: 0; box-sizing: border-box; }
  html, body { width: 1200px; height: 892px; overflow: hidden; }
  body {
    background: var(--backdrop);
    display: flex;
    flex-direction: column;
    align-items: center;
    justify-content: center;
    gap: 36px;
    font-family: "Arimo", Arial, sans-serif;
  }
  .card {
    position: relative;
    width: 700px;
    height: 400px;
    overflow: hidden;
    box-shadow: 0 10px 28px rgba(0,0,0,0.28);
  }

  /* Info side */
  .card-info { background: var(--ink); color: var(--paper); }
  .card-info .edge-band {
    position: absolute; left: 0; right: 0; bottom: 0; height: 42px;
  }
  .card-info .brand {
    position: absolute; left: 48px; top: 200px;
    font-family: "Arimo", Arial, sans-serif;
    font-weight: 700; font-size: 62px; letter-spacing: 1px;
    color: var(--paper);
  }
  .card-info .divider {
    position: absolute; left: 338px; top: 48px;
    width: 1px; height: 270px; background: var(--rule);
  }
  .card-info .details {
    position: absolute; left: 368px; top: 66px;
  }
  .card-info .name {
    font-family: "Tinos", "Times New Roman", serif;
    font-weight: 700; font-size: 31px; margin-bottom: 22px;
  }
  .contact-list { list-style: none; }
  .contact-list li {
    display: flex; align-items: center; gap: 12px;
    font-size: 16px; line-height: 30px; white-space: nowrap;
  }
  .contact-list svg { flex: none; }

  /* Logo side */
  .card-logo {
    background: radial-gradient(ellipse at 45% 40%, var(--paper) 55%, var(--paper-shade) 100%);
    color: var(--ink);
    display: flex; align-items: center; justify-content: center;
  }
  .card-logo .brand {
    font-family: "Arimo", Arial, sans-serif;
    font-weight: 700; font-size: 118px; letter-spacing: 2px;
    margin-top: -20px;
  }
  .card-logo .edge-band {
    position: absolute; left: 0; right: 0; bottom: 0; height: 30px;
  }
</style>
</head>
<body>

<section class="card card-info">
  <div class="brand">Q-Rolls</div>
  <div class="divider"></div>
  <div class="details">
    <div class="name">Tomas Velder</div>
    <ul class="contact-list">
      <li>
        <svg width="14" height="14" viewBox="0 0 14 14" aria-hidden="true"><rect width="14" height="14" fill="#fff"/><rect x="4" y="2" width="6" height="10" rx="1" fill="#000"/></svg>
        630-812-4463
      </li>
      <li>
        <svg width="14" height="14" viewBox="0 0 14 14" aria-hidden="true"><rect width="14" height="14" fill="#fff"/><path d="M3 4h8v6H3z" fill="#000"/><rect x="5" y="3" width="4" height="2" fill="#000"/></svg>
        630-917-3384 EXT. 417
      </li>
      <li>
        <svg width="14" height="14" viewBox="0 0 14 14" aria-hidden="true"><rect width="14" height="14" fill="#fff"/><path d="M2.5 4h9v6h-9z M2.5 4l4.5 3.5L11.5 4" fill="none" stroke="#000" stroke-width="1.2"/></svg>
        Tomas@q-rolls-example.com
      </li>
      <li>
        <svg width="14" height="14" viewBox="0 0 14 14" aria-hidden="true"><rect width="14" height="14" fill="#fff"/><circle cx="7" cy="7" r="4" fill="none" stroke="#000" stroke-width="1.2"/><path d="M3 7h8M7 3v8" stroke="#000" stroke-width="1"/></svg>
        www.Q-rolls-example.com
      </li>
    </ul>
  </div>
  <svg class="edge-band" viewBox="0 0 700 42" preserveAspectRatio="none" aria-hidden="true">
    <rect x="0" y="6" width="700" height="3" fill="#fff"/>
    <rect x="0" y="16" width="700" height="26" fill="#fff"/>
    <rect x="0" y="24" width="700" height="2" fill="#000"/>
  </svg>
</section>

<section class="card card-logo">
  <div class="brand">Q-Rolls</div>
  <svg class="edge-band" viewBox="0 0 700 30" preserveAspectRatio="none" aria-hidden="true">
    <rect x="0" y="8" width="700" height="3" fill="#0b0b0b"/>
    <rect x="0" y="18" width="700" height="12" fill="#0b0b0b"/>
  </svg>
</section>

</body>
</html>
```